32 x 24 Swinging Real Estate Yard Sign

We are looking to design a new sign for our business to focus on the remodeling of homes to sell. We are looking to have a yard sign that gets peoples attention and is informational. The headline will be "The Secret to Top Dollar? Remodel First.". We remodel homes for sellers with no up front cost, as they simply pay at closing. This link has more info, https://brightkeelhomes.com/Remodel
The message we want to convey to those seeing the sign is we are a one stop shop, who can renovate your home and sell it for no stress. We are licensed real estate agents and licensed contractors.
Both of these license numbers and info need to be on the design:
CADRE #02741968
Contractors License #2758314
Email: info@brightkeelhomes.com
Phone: (408)514-7290
I'll attach a sample sign we have for our agents normally as well as all brand art work.
• Pantone Colors
o #172A41
Dark blue
o #4381B1
Medium blue
o #6FA6CC
Light blue
Target Market(s)
Residential Real Estate Sellers
Industry/Entity Type
Real Estate
Colors
Designer to choose colors to be used in the design.

```html
<!DOCTYPE html>
<html lang="en">
<head>
<meta charset="utf-8">
<title>Brightkeel Homes – Yard Sign</title>
<link href="https://fonts.googleapis.com/css2?family=Montserrat:wght@400;500;600;700;800;900&display=swap" rel="stylesheet">
<style>
  :root {
    --dark-blue: #172A41;
    --medium-blue: #4381B1;
    --light-blue: #6FA6CC;
    --white: #FFFFFF;
    --backdrop: #C6C6C6;
  }
  * { margin: 0; padding: 0; box-sizing: border-box; }
  html, body {
    width: 1200px;
    height: 1056px;
    overflow: hidden;
    background: var(--backdrop);
    font-family: 'Montserrat', sans-serif;
  }
  .yard-sign {
    position: absolute;
    left: 40px;
    top: 108px;
    width: 1120px;
    height: 840px;
    display: flex;
    flex-direction: column;
  }
  .brand-band {
    height: 281px;
    background: var(--white);
    display: flex;
    align-items: center;
    justify-content: center;
    gap: 28px;
  }
  .brand-dot {
    width: 84px;
    height: 84px;
    border-radius: 50%;
    background: var(--medium-blue);
  }
  .brand-name {
    font-weight: 600;
    font-size: 76px;
    letter-spacing: 1px;
    color: var(--dark-blue);
    text-transform: uppercase;
  }
  .headline-band {
    height: 280px;
    background: var(--medium-blue);
    display: flex;
    flex-direction: column;
    align-items: center;
    justify-content: center;
    line-height: 1;
  }
  .headline-lead {
    font-weight: 500;
    font-size: 108px;
    color: var(--white);
    letter-spacing: 1px;
  }
  .headline-main {
    margin-top: 12px;
    font-weight: 900;
    font-size: 114px;
    color: var(--dark-blue);
    letter-spacing: -1px;
  }
  .dollar-o {
    display: inline-block;
    width: 0.82em;
    height: 0.82em;
    margin: 0 0.02em;
    border-radius: 50%;
    background: var(--dark-blue);
    color: var(--white);
    font-weight: 500;
    font-size: 1em;
    line-height: 0.82em;
    text-align: center;
    vertical-align: -0.06em;
  }
  .dollar-o span { font-size: 0.55em; vertical-align: 0.25em; }
  .contact-band {
    height: 279px;
    background: var(--dark-blue);
    display: flex;
    flex-direction: column;
    align-items: center;
    justify-content: center;
    gap: 22px;
  }
  .phone-line {
    display: flex;
    align-items: center;
    gap: 10px;
    color: var(--white);
    font-weight: 700;
    font-size: 104px;
    line-height: 1;
    letter-spacing: -1px;
  }
  .phone-icon { width: 84px; height: 84px; }
  .details-line {
    display: flex;
    align-items: center;
    gap: 18px;
    color: var(--medium-blue);
  }
  .email { font-size: 38px; font-weight: 400; }
  .divider {
    width: 3px;
    height: 34px;
    background: var(--white);
  }
  .licenses {
    font-size: 18px;
    font-weight: 400;
    line-height: 1.3;
  }
  .licenses strong { font-weight: 700; }
</style>
</head>
<body>
  <main class="yard-sign">
    <header class="brand-band">
      <div class="brand-dot"></div>
      <div class="brand-name">Brightkeel Homes</div>
    </header>

    <section class="headline-band">
      <h1 class="headline-lead">THE SECRET TO</h1>
      <p class="headline-main">TOP D<span class="dollar-o"><span>$</span></span>LLAR?</p>
    </section>

    <footer class="contact-band">
      <div class="phone-line">
        <svg class="phone-icon" viewBox="0 0 100 100" aria-hidden="true">
          <path fill="#FFFFFF" d="M22 8 c5-3 9-2 12 2 l10 14 c3 4 2 8-1 11 l-7 6 c4 10 12 20 23 27 l7-6 c3-3 7-3 11 0 l13 11 c4 3 4 7 1 11 l-6 7 c-4 4-10 5-16 3 C46 86 18 60 8 32 C6 25 8 19 13 15 Z"/>
          <path fill="none" stroke="#FFFFFF" stroke-width="6" stroke-linecap="round" d="M58 22 a22 22 0 0 1 20 20"/>
          <path fill="none" stroke="#FFFFFF" stroke-width="6" stroke-linecap="round" d="M60 6 a38 38 0 0 1 34 34"/>
        </svg>
        <span class="phone-number">(408)514-7290</span>
      </div>
      <div class="details-line">
        <span class="email">info@brightkeelhomes.com</span>
        <span class="divider"></span>
        <div class="licenses">
          <div>CADRE <strong>#02741968</strong></div>
          <div>Contractors License <strong>#2758314</strong></div>
        </div>
      </div>
    </footer>
  </main>
</body>
</html>
```